Business Card Design Project for Food Export Company

Introduction about my Company Lin Kai Trading Pte. Ltd.
(Lin Kai Food Trading)
A Sole Distributor of various products:
Brand
Soy Powder (Brand: Beanette)
Coffee Powders (Brand: Rovo)
OEM products
- Cocoa Powder
- Green Tea Powder
- Almond Powder
- Almond Flavour Powder
Showing we are professional with decades of experiences in terms of Product Quality and Trust.
NAMECARD - 2 sided namecard
Front:
Informations:
Marcus Tan
Sales Executive
+65 90000000
marcustan@lkfoodtrade.com
Lin Kai Trading Pte. Ltd.
42 Tampines Road, #03-08 Horizon Centre
Singapore 520000
Back:
Sole Distributor:
Beanette and Rovo
OEM Products:
Cocoa Powder / Green Tea Powder / Almond Powder / Almond Flavour Powder / Ice Cream Powder
I have attached Lin Kai Trading's Logos. I've 2 currently, I would like to see some comparison.
Attached 2 Logos for Rovo and Beanette.
Updates
Hi all designers,
I've revised the brief.
Have a look.
Thank you
Marcus

```html
<!DOCTYPE html>
<html lang="en">
<head>
<meta charset="utf-8">
<title>Lin Kai Food Trading — Business Card</title>
<link href="https://fonts.googleapis.com/css2?family=Cinzel:wght@400;600&family=Arimo:wght@700&display=swap" rel="stylesheet">
<style>
  :root {
    --bg: #d9d9d9;
    --card: #050505;
    --gold: #d9a63a;
    --gold-light: #f6dc6a;
    --gold-deep: #9c6a1c;
    --text-gold: #d8a24a;
    --rule: #8a7a55;
  }
  * { margin: 0; padding: 0; box-sizing: border-box; }
  html, body { width: 1200px; height: 1000px; overflow: hidden; }
  body {
    background: radial-gradient(ellipse at 50% 45%, #eeeeee 0%, var(--bg) 70%, #bdbdbd 100%);
    font-family: "Cinzel", Georgia, serif;
    color: var(--text-gold);
    position: relative;
  }
  .card {
    position: absolute;
    top: 350px;
    width: 525px;
    height: 300px;
    background: var(--card);
    border: 2px solid var(--gold);
    overflow: hidden;
    box-shadow: 0 18px 30px rgba(0,0,0,0.35);
  }
  .card--back { left: 50px; }
  .card--front { left: 625px; }
  .card__corner { position: absolute; }
  .card--back .card__corner { left: 0; bottom: 0; width: 110px; height: 160px; }
  .card--front .card__corner { right: 0; top: 0; width: 110px; height: 150px; }

  .brand {
    position: absolute;
    width: 175px;
    text-align: center;
  }
  .card--back .brand { left: 50px; top: 70px; }
  .card--front .brand { left: 40px; top: 70px; }
  .brand__name {
    font-family: "Cinzel", Georgia, serif;
    font-weight: 600;
    font-size: 34px;
    color: var(--gold-light);
    line-height: 1.1;
    padding-bottom: 6px;
    border-bottom: 1px solid var(--rule);
  }
  .brand__sub {
    font-size: 13px;
    letter-spacing: 2px;
    margin-top: 4px;
  }
  .brand__en {
    font-size: 17px;
    letter-spacing: 4px;
  }
  .brand__tagline {
    font-size: 9px;
    letter-spacing: 0.5px;
    line-height: 1.2;
    margin-top: 4px;
    padding-bottom: 4px;
    border-bottom: 1px solid var(--rule);
  }

  .offer {
    position: absolute;
    left: 285px;
    top: 92px;
    width: 225px;
  }
  .offer__heading { font-size: 17px; margin-bottom: 8px; }
  .offer__brands { font-size: 15px; margin-bottom: 10px; }
  .offer__label { font-size: 13px; margin-bottom: 4px; }
  .offer__list { list-style: none; font-size: 11px; line-height: 1.25; }

  .person {
    position: absolute;
    left: 260px;
    top: 100px;
  }
  .person__name {
    font-family: "Arimo", Arial, sans-serif;
    font-weight: 700;
    font-size: 20px;
    letter-spacing: 2px;
    color: #e39a2e;
  }
  .person__title {
    font-family: "Arimo", Arial, sans-serif;
    font-weight: 700;
    font-size: 12px;
    letter-spacing: 2px;
    margin-top: 4px;
    color: #e39a2e;
  }
  .contact {
    position: absolute;
    left: 260px;
    top: 172px;
    list-style: none;
    font-size: 10.5px;
    line-height: 1.7;
  }
  .address {
    position: absolute;
    left: 0;
    right: 0;
    top: 238px;
    text-align: center;
    font-size: 12px;
    line-height: 1.6;
  }
</style>
</head>
<body>

  <section class="card card--back" aria-label="Card back">
    <svg class="card__corner" viewBox="0 0 110 160" aria-hidden="true">
      <defs>
        <linearGradient id="goldBack" x1="0" y1="0" x2="1" y2="1">
          <stop offset="0" stop-color="#f6dc6a"/>
          <stop offset="0.55" stop-color="#d9a63a"/>
          <stop offset="1" stop-color="#9c6a1c"/>
        </linearGradient>
      </defs>
      <polygon points="0,0 110,160 0,160" fill="url(#goldBack)"/>
    </svg>

    <div class="brand">
      <div class="brand__name">Lin Kai</div>
      <div class="brand__sub">Food Trading</div>
      <div class="brand__en">LIN KAI</div>
      <div class="brand__tagline">Sole distributor of<br>various quality products</div>
    </div>

    <div class="offer">
      <p class="offer__heading">Sole Distributor</p>
      <p class="offer__brands">Beanette and Rovo</p>
      <p class="offer__label">OEM Products:</p>
      <ul class="offer__list">
        <li>Cocoa Powder</li>
        <li>Green Tea Powder</li>
        <li>Almond Powder</li>
        <li>Almond Flavour Powder</li>
        <li>Ice Cream Powder</li>
      </ul>
    </div>
  </section>

  <section class="card card--front" aria-label="Card front">
    <svg class="card__corner" viewBox="0 0 110 150" aria-hidden="true">
      <defs>
        <linearGradient id="goldFront" x1="0" y1="0" x2="1" y2="1">
          <stop offset="0" stop-color="#f6dc6a"/>
          <stop offset="0.55" stop-color="#d9a63a"/>
          <stop offset="1" stop-color="#9c6a1c"/>
        </linearGradient>
      </defs>
      <polygon points="0,0 110,0 110,150" fill="url(#goldFront)"/>
    </svg>

    <div class="brand">
      <div class="brand__name">Lin Kai</div>
      <div class="brand__sub">Food Trading</div>
      <div class="brand__en">LIN KAI</div>
      <div class="brand__tagline">Sole distributor of<br>various quality products</div>
    </div>

    <div class="person">
      <p class="person__name">MARCUS TAN</p>
      <p class="person__title">SALES EXECUTIVE</p>
    </div>

    <ul class="contact">
      <li>E : marcustan@lkfoodtrade.com</li>
      <li>W: www.lkfoodtrade.com</li>
      <li>C: +65 90000000</li>
    </ul>

    <p class="address">42 Tampines Road, #03-08 Horizon Centre<br>Singapore 520000</p>
  </section>

</body>
</html>
```